Wine Bottle Label Logo Design

My fiancé and I are getting married in September and we made homemade wine which will be given to the guests as a wedding favor. We need label/logo for our wine bottles. We were looking for something rustic yet modern and simple. We had an idea for beige and cranberry colored wine stained, weathered, imperfect heart. Things that will need to be incorporated into the label design are as follows:
Our last name and also the name of the wine: Bastoni
The year: 2012
Where is says Alcohol Content on a wine bottle normally write: Alcohol: Deceiving% by vol.
Type of wine: Red Wine
Incorporate our wedding date: Foot Stomped and Bottled for Jess and Ned's Wedding Day 9/28/13

```html
<!DOCTYPE html>
<html lang="en">
<head>
<meta charset="utf-8">
<title>Bastoni Red Wine Label</title>
<link rel="stylesheet" href="https://fonts.googleapis.com/css2?family=Cinzel:wght@700&family=Libre+Baskerville:ital,wght@1,700&family=PT+Sans:wght@400;700&display=swap">
<style>
  :root {
    --backdrop-top: #f4f4f4;
    --backdrop-bottom: #1c1c1c;
    --cranberry: #b3203f;
    --cranberry-deep: #7a1020;
    --ribbon-red: #6e0f1a;
    --beige: #f1e4c6;
    --beige-light: #fbf3df;
    --gold: #b8904a;
    --gold-light: #e3c88a;
    --ink: #3b2a1c;
    --blush: #f3c6cb;
  }
  html, body {
    margin: 0;
    padding: 0;
    width: 1200px;
    height: 1000px;
    overflow: hidden;
  }
  body {
    background: linear-gradient(to bottom, var(--backdrop-top), var(--backdrop-bottom));
  }
  .label-art {
    display: block;
    width: 1200px;
    height: 1000px;
  }
  .abv {
    font-family: "PT Sans", sans-serif;
    font-weight: 700;
    font-size: 20px;
    fill: var(--ink);
  }
  .edition {
    font-family: "PT Sans", sans-serif;
    font-weight: 700;
    font-size: 24px;
    letter-spacing: 1px;
    fill: var(--cranberry);
  }
  .wine-name {
    font-family: "Cinzel", serif;
    font-weight: 700;
    font-size: 92px;
    fill: var(--gold);
  }
  .dedication {
    font-family: "PT Sans", sans-serif;
    font-weight: 700;
    font-size: 23px;
    fill: var(--ink);
  }
  .wine-type {
    font-family: "Libre Baskerville", serif;
    font-style: italic;
    font-weight: 700;
    font-size: 34px;
    fill: var(--cranberry-deep);
  }
  .wedding-date {
    font-family: "PT Sans", sans-serif;
    font-weight: 700;
    font-size: 28px;
    fill: var(--blush);
  }
</style>
</head>
<body>
<svg class="label-art" viewBox="0 0 1200 1000" xmlns="http://www.w3.org/2000/svg">
  <defs>
    <linearGradient id="gold-band" x1="0" y1="0" x2="0" y2="1">
      <stop offset="0" stop-color="#e6cf98"/>
      <stop offset="0.5" stop-color="#b8904a"/>
      <stop offset="1" stop-color="#8a6630"/>
    </linearGradient>
    <radialGradient id="diamond-fill" cx="0.5" cy="0.45" r="0.6">
      <stop offset="0" stop-color="#fbf3df"/>
      <stop offset="1" stop-color="#ead9b2"/>
    </radialGradient>
  </defs>

  <!-- cranberry badge -->
  <path class="badge" d="M360 110 Q600 70 840 110 Q858 150 905 160 L905 560 Q905 845 600 845 Q295 845 295 560 L295 160 Q342 150 360 110 Z"
        fill="var(--cranberry)" stroke="var(--gold-light)" stroke-width="4"/>
  <path class="badge-inner-line" d="M368 126 Q600 90 832 126 Q850 160 889 172 L889 560 Q889 829 600 829 Q311 829 311 560 L311 172 Q350 160 368 126 Z"
        fill="none" stroke="var(--cranberry-deep)" stroke-width="3"/>

  <!-- hanging ribbon tail -->
  <path class="ribbon-tail" d="M545 640 L655 640 L655 965 L600 915 L545 965 Z" fill="var(--ribbon-red)"/>

  <!-- beige diamond -->
  <path class="diamond" d="M600 118 L872 420 L600 722 L328 420 Z" fill="var(--gold)"/>
  <path class="diamond-face" d="M600 134 L857 420 L600 706 L343 420 Z" fill="url(#diamond-fill)" stroke="var(--cranberry-deep)" stroke-width="2"/>

  <!-- mark placeholder -->
  <circle class="mark" cx="600" cy="222" r="20" fill="none" stroke="var(--gold)" stroke-width="4"/>

  <text class="abv" x="600" y="270" text-anchor="middle">Deceiving% by vol.</text>
  <text class="edition" x="600" y="302" text-anchor="middle">2012 EDITION</text>
  <text class="wine-name" x="600" y="425" text-anchor="middle">Bastoni</text>
  <text class="dedication" x="600" y="490" text-anchor="middle">Foot Stomped and Bottled</text>
  <text class="dedication" x="600" y="518" text-anchor="middle">for Jess and Ned's</text>

  <!-- gold banner -->
  <path class="banner-end" d="M372 590 L420 582 L420 632 L372 640 L390 614 Z" fill="#8a6630"/>
  <path class="banner-end" d="M828 590 L780 582 L780 632 L828 640 L810 614 Z" fill="#8a6630"/>
  <path class="banner" d="M400 566 Q600 540 800 566 L800 622 Q600 596 400 622 Z" fill="url(#gold-band)" stroke="var(--cranberry-deep)" stroke-width="1.5"/>
  <text class="wine-type" x="600" y="597" text-anchor="middle">Red Wine</text>

  <text class="wedding-date" x="600" y="768" text-anchor="middle">Wedding Day 9/28/13</text>
</svg>
</body>
</html>
```